Ansprechendes Layout für Geschichte von Oldtimern
Grossartiges Design, supernette Zusammenarbeit, megaschnelle Rückmeldung auf meine dusseligen Fragen - dass "Kastrel Ubo" sich meines Projektes angenommen hat, war ein echter Glückstreffer! Ich bin sowohl mit dem Ergebnis als auch mit der Kommunikation während des gesamten Prozesses absolut happy! Das hat richtig Spaß gemacht und auf meine Oldtimer-"Broschüre" bin ich stolz wie Bolle... Schade, dass man hier nicht 10 Sterne vergeben kann - "Kastrel Ubo" hätte sie verdient!
Zielgruppe
Ich mache mich aktuell selbstständig als Solo-Freiberuflerin (Redakteurin) mit dem Projekt 'Die Lack-Ballade': Ich schreibe für Oldtimer-Besitzer die Lebensgeschichte ihres Oldtimers auf - lebendig und augenzwinkernd. Zielgruppe: Oldtimer-Besitzer, die die Historie ihres Wagens als individuelles 'Buch' haben möchten; für sich selbst oder auch als Verkaufsargument beim Weiterverkauf des Oldtimers.
Aufgabenstellung
Mein Text wird auf hochwertigem Papier (einseitig) gedruckt , im Format A4 quer. Ein paar gut platzierte Fotos sollen den Text 'auflockern'. Für dieses Layout von Titelseite sowie Text & Fotos suche ein 'hinreißendes' Design (Schriften und Layout). Die fertigen Seiten werden dann in einer Druckerei ausgedruckt und in einen A4 Querformat-Klemmbinder 'reingesteckt'. Deswegen muss links entsprechend viel Rand/Platz gelassen werden. Wichtig ist mir eine sehr edle und hochwertige Anmutung des Layouts. Es soll kein 'Bildband' werden, die Fotos ergänzen lediglich den Text, der 'im Mittelpunkt' steht.

```html
<!DOCTYPE html>
<html lang="de">
<head>
<meta charset="utf-8">
<title>Die Lack-Ballade – Seiten</title>
<link href="https://fonts.googleapis.com/css2?family=Open+Sans:wght@400&display=swap" rel="stylesheet">
<style>
  :root {
    --gold: #b7a25c;
    --ink: #1c1c1c;
    --muted: #6b6b6b;
    --band-dark: #333333;
    --paper: #ffffff;
    --backdrop: #ffffff;
  }
  html, body {
    margin: 0;
    padding: 0;
    width: 1200px;
    height: 2554px;
    overflow: hidden;
    background: var(--backdrop);
  }
  .canvas {
    position: relative;
    width: 1200px;
    height: 2554px;
  }
  .page {
    position: absolute;
    left: 46px;
    width: 1110px;
    height: 786px;
    background: var(--paper);
    box-shadow: 3px 4px 6px rgba(0,0,0,0.35);
    overflow: hidden;
  }
  .page--one { top: 62px; }
  .page--two { top: 888px; }
  .page--three { top: 1721px; }

  .page__top-band {
    position: absolute; left: 0; top: 0; width: 100%; height: 13px;
    background: var(--band-dark);
  }
  .page__bottom-band {
    position: absolute; left: 0; bottom: 0; width: 100%; height: 30px;
    background: var(--gold);
  }

  .brand {
    position: absolute;
    right: 76px;
    top: 70px;
    text-align: right;
    font-family: "Open Sans", sans-serif;
  }
  .brand__name {
    display: flex;
    align-items: center;
    justify-content: flex-end;
    gap: 12px;
    color: var(--gold);
    font-size: 32px;
    line-height: 40px;
    font-weight: 400;
  }
  .brand__square {
    width: 14px;
    height: 14px;
    background: var(--gold);
    flex: none;
  }
  .brand__tagline {
    margin-top: 8px;
    font-size: 12px;
    letter-spacing: 1.5px;
    color: var(--muted);
  }

  .story {
    position: absolute;
    margin: 0;
    font-family: "Open Sans", sans-serif;
    font-size: 14px;
    line-height: 19.8px;
    color: var(--ink);
    text-align: justify;
  }
  .photo {
    position: absolute;
    display: block;
  }

  .page--one .photo { left: 117px; top: 327px; width: 365px; height: 250px; }
  .page--one .story { left: 522px; top: 322px; width: 512px; }

  .page--two .story--left { left: 117px; top: 342px; width: 428px; }
  .page--two .story--right { left: 605px; top: 342px; width: 428px; }

  .page--three .photo { left: 117px; top: 284px; width: 917px; height: 150px; }
  .page--three .story { left: 117px; top: 460px; width: 917px; }
</style>
</head>
<body>
<div class="canvas">

  <section class="page page--one">
    <div class="page__top-band"></div>
    <div class="brand">
      <div class="brand__name"><span class="brand__square"></span><span>Die Lack-Ballade</span></div>
      <div class="brand__tagline">LEBENSGESCHICHTEN FÜR OLDTIMER</div>
    </div>
    <svg class="photo" role="img" aria-label="Foto: weißes Lenkrad eines Oldtimers im dunklen Innenraum" viewBox="0 0 365 250" preserveAspectRatio="none">
      <defs>
        <linearGradient id="interior" x1="0" y1="0" x2="1" y2="1">
          <stop offset="0" stop-color="#2c3333"/>
          <stop offset="0.5" stop-color="#5a5f5c"/>
          <stop offset="1" stop-color="#1e2424"/>
        </linearGradient>
      </defs>
      <rect width="365" height="250" fill="url(#interior)"/>
    </svg>
    <p class="story">Zwanzig Jahre lang habe ich also den Herrn Kerbel-Generaldirektor von Hamburg aus kreuz und quer durch Norddeutschland gefahren – sicher, butterweich gefedert, und selbstverständlich immer zuverlässig. Man weiß ja schließlich, was sich gehört. So als Heckflossen-Valdor im Auftrag eines weltweit bekannten Unternehmens. Der nette Chauffeur vom Chef hat mich dann eines Tages übernommen, als die Firma meinte, mich doch tatsächlich durch ein jüngeres Modell ersetzen zu müssen. Frechheit, oder?! Und dann hat mich der Sohn vom Chauffeur übernommen, als sein alter Herr nicht mehr so gut Auto fahren konnte. Irgendwann war ich auch mal kurzfristig in den sanften Händen einer schönen Frau, die mich leider aber nur kurz behalten hat. Bitte entschuldige, dass ich auf meine alten Tage doch leider vergessen habe, warum ich die elegante Lady nicht länger durch die Welt fahren durfte – ich fand, wir waren wirklich ein schönes Paar und passten gut zusammen.</p>
    <div class="page__bottom-band"></div>
  </section>

  <section class="page page--two">
    <div class="page__top-band"></div>
    <div class="brand">
      <div class="brand__name"><span class="brand__square"></span><span>Die Lack-Ballade</span></div>
      <div class="brand__tagline">LEBENSGESCHICHTEN FÜR OLDTIMER</div>
    </div>
    <p class="story story--left">An den fünften Besitzer habe ich noch jede Menge Erinnerungen: Er hat es richtig gut gemeint mit mir und mich einer regelrechten Verjüngungskur unterzogen. Eine neue Lackierung! Die Technik mal so richtig überholt! Neue Türen! Ach, welch herrliches Wohlbefinden für mein altes Blech…! Ich erstrahlte in neuem Glanz und fühlte mich gleich wieder viel jünger. Nun ja, und so war es ja dann wohl auch kein Wunder, dass sich erst der Jochen und dann der Henrik in mich verliebten – schließlich war diese Behandlung ja der reinste Jungbrunnen für mich! Dem Rest von Henriks Familie habe ich dann ja auch alsbald den Kopf verdreht. Auf meine ganz persönliche Weise: Ich bin ja nicht so der laute</p>
    <p class="story story--right">oder gar prahlerische Typ – ich punkte auf meine ganz eigene, unnachahmliche Art. Mit Charakter, Eleganz, Zuverlässigkeit und Ehrlichkeit. Und natürlich mit meinem ganz besonderen Charme – der hat zuverlässig noch jede Frau umgehauen… Die Frau und die Tochter vom Henrik hat’s jedenfalls alle beide ganz schön erwischt: Die eine schwört, dass ich zur Familie gehöre und niemals weiterverkauft werde. Die andere hat schon angekündigt, dass als ihr zukünftiges Hochzeitsauto nur ein Wagen in Frage kommt: ich. Zugegeben: So gefällt mir das! Diese Wertschätzung ist voll und ganz nach meinem Geschmack.</p>
    <div class="page__bottom-band"></div>
  </section>

  <section class="page page--three">
    <div class="page__top-band"></div>
    <div class="brand">
      <div class="brand__name"><span class="brand__square"></span><span>Die Lack-Ballade</span></div>
      <div class="brand__tagline">LEBENSGESCHICHTEN FÜR OLDTIMER</div>
    </div>
    <svg class="photo" role="img" aria-label="Foto: Front eines schwarzen Oldtimers mit Scheinwerfern und Kühlergrill" viewBox="0 0 917 150" preserveAspectRatio="none">
      <defs>
        <linearGradient id="front" x1="0" y1="0" x2="1" y2="0">
          <stop offset="0" stop-color="#3a3226"/>
          <stop offset="0.2" stop-color="#141820"/>
          <stop offset="0.5" stop-color="#6f7276"/>
          <stop offset="0.8" stop-color="#141820"/>
          <stop offset="1" stop-color="#3a3226"/>
        </linearGradient>
      </defs>
      <rect width="917" height="150" fill="url(#front)"/>
    </svg>
    <p class="story">Henriks Sohn hat mich ebenfalls längst ins Herz geschlossen. Und ich ihn auch. Aber der junge Herr war am Anfang ein bisschen zu ungestüm in seinem jugendlichen Elan: Einsteigen, Joke ziehen, Zündung an und zack – losfahren? Nein, mein Junge, so läuft das bei mir nicht. Da habe ich mich zum ersten Mal schlicht und einfach geweigert, anzuspringen. Hab’ ich vorher noch nie gemacht. Ehrenwort! Gehört sich einfach nicht als Valdor. Aber in diesem Fall musste ich doch mal eine Ausnahme machen und dem jungen Mann Manieren beibringen: Immer mit der Ruhe. Wenn wir zusammen unterwegs sind, wünsche ich mir, dass sich mein Fahrer ein kleines bisschen von mir verzaubern lässt – für das wunderbare Erlebnis einer kleinen Zeitreise, die eine Fahrt mit mir immer auch bedeutet. Glücklicherweise hat er das auch ganz schnell verstanden. Und der Henrik hat ihm das in einer ruhigen Minute auch nochmal erklärt: „Das Fahren mit diesem Wagen entschleunigt ungemein. Du vergisst Hektik und Stress. Du gleitest einfach sanft dahin – je länger, desto entspannter. Irgendwann spielt Zeit keine Rolle mehr.“ Genau. Ich hätte es nicht besser ausdrücken können, lieber Henrik. Danke.</p>
    <div class="page__bottom-band"></div>
  </section>

</div>
</body>
</html>
```